Business Card Design Project

Want a modern business card.
Concern is that our email address is long and thus poses a design challenge.
Items like the company name can be omitted from text as it will be available via the logo.

Example:
Gerald Tunstall
President / CEO
Cell 555.304.1182
Office 555.617.2093
geraldt@korvantsolutionsgroup.example
www.korvantsolutionsgroup.example

Target Market(s)

Technical and executive level members of Information Technology companies in the Healthcare industry.

Industry/Entity Type

Business

Colors

Designer to choose colors to be used in the design.

Requirements
Nice to have
• Raised logo, but I am open.

```html
<!DOCTYPE html>
<html lang="en">
<head>
<meta charset="utf-8">
<title>Korvant Solutions Group — Business Card</title>
<link rel="stylesheet" href="https://fonts.googleapis.com/css2?family=Arimo:wght@400;700&display=swap">
<style>
  :root {
    --navy: #0b2d86;
    --red: #e0101e;
    --paper: #ffffff;
    --backdrop: #e7e5e2;
    --rule: #c9c9c9;
    --shadow: rgba(0, 0, 0, 0.18);
  }
  * { box-sizing: border-box; margin: 0; padding: 0; }
  html, body {
    width: 1200px;
    height: 960px;
    overflow: hidden;
    background: var(--backdrop);
    font-family: "Arimo", Arial, sans-serif;
  }
  .canvas {
    width: 1200px;
    height: 960px;
    display: flex;
    flex-direction: column;
    align-items: center;
    justify-content: center;
    gap: 44px;
  }
  .card {
    position: relative;
    width: 735px;
    height: 420px;
    background: var(--paper);
    box-shadow: 0 6px 18px var(--shadow);
    overflow: hidden;
  }

  /* Wordmark */
  .wordmark {
    display: flex;
    align-items: center;
    gap: 14px;
    color: var(--navy);
    font-weight: 700;
    text-transform: uppercase;
    line-height: 1;
    white-space: nowrap;
  }
  .wordmark-square {
    width: 18px;
    height: 18px;
    background: var(--red);
    flex: none;
  }
  .wordmark-name {
    font-size: 34px;
    letter-spacing: 0.04em;
  }

  /* Front */
  .card-front .wordmark {
    position: absolute;
    left: 0; right: 0;
    top: 160px;
    justify-content: center;
  }
  .card-front .website {
    position: absolute;
    right: 70px;
    bottom: 70px;
    color: var(--navy);
    font-size: 19px;
  }

  /* Back */
  .card-back .wordmark {
    position: absolute;
    left: 34px;
    top: 172px;
    width: 390px;
    gap: 10px;
  }
  .card-back .wordmark-square { width: 14px; height: 14px; }
  .card-back .wordmark-name {
    font-size: 21px;
    letter-spacing: 0.02em;
  }
  .divider {
    position: absolute;
    left: 452px;
    top: 60px;
    width: 1px;
    height: 220px;
    background: var(--rule);
  }
  .contact {
    position: absolute;
    left: 486px;
    top: 62px;
  }
  .contact-name {
    color: var(--navy);
    font-weight: 700;
    font-size: 21px;
  }
  .contact-title {
    color: var(--red);
    font-size: 13px;
    margin-top: 3px;
  }
  .phones {
    list-style: none;
    margin-top: 48px;
    display: flex;
    flex-direction: column;
    gap: 14px;
  }
  .phone {
    display: flex;
    align-items: center;
    gap: 12px;
    color: var(--navy);
    font-size: 19px;
  }
  .phone svg { width: 18px; height: 18px; flex: none; }

  .band {
    position: absolute;
    left: 0; right: 0;
    bottom: 30px;
    height: 68px;
    background: var(--navy);
    display: flex;
    align-items: center;
    padding-left: 34px;
  }
  .band-email {
    color: var(--paper);
    font-size: 21px;
  }
  .band-stripe {
    position: absolute;
    left: 0; right: 0;
    bottom: 18px;
    height: 12px;
    background: var(--red);
  }
</style>
</head>
<body>
<main class="canvas">

  <section class="card card-front" aria-label="Card front">
    <div class="wordmark">
      <span class="wordmark-square"></span>
      <span class="wordmark-name">Korvant Solutions Group</span>
    </div>
    <p class="website">www.korvantsolutionsgroup.example</p>
  </section>

  <section class="card card-back" aria-label="Card back">
    <div class="wordmark">
      <span class="wordmark-square"></span>
      <span class="wordmark-name">Korvant Solutions Group</span>
    </div>

    <div class="divider"></div>

    <div class="contact">
      <p class="contact-name">Gerald Tunstall</p>
      <p class="contact-title">President / CEO</p>
      <ul class="phones">
        <li class="phone">
          <svg viewBox="0 0 18 18" aria-label="Cell">
            <rect x="4" y="1" width="10" height="16" rx="2" fill="var(--red)"/>
            <rect x="6" y="3.5" width="6" height="6" fill="#fff"/>
            <circle cx="9" cy="13.5" r="1.3" fill="#fff"/>
          </svg>
          <span>555.304.1182</span>
        </li>
        <li class="phone">
          <svg viewBox="0 0 18 18" aria-label="Office">
            <path d="M2 6 Q9 1 16 6 L14.5 8 L12 7 L12 5.5 Q9 4.5 6 5.5 L6 7 L3.5 8 Z" fill="var(--red)"/>
            <path d="M5 9 L13 9 L15 16 L3 16 Z" fill="var(--red)"/>
            <circle cx="9" cy="12.5" r="1.8" fill="#fff"/>
          </svg>
          <span>555.617.2093</span>
        </li>
      </ul>
    </div>

    <div class="band">
      <p class="band-email">geraldt@korvantsolutionsgroup.example</p>
    </div>
    <div class="band-stripe"></div>
  </section>

</main>
</body>
</html>
```